Photography and Videography - Brightwell Studios - New Business Card Design

Brightwell Studios is a photography and Videography Company started by creative couple Robby K and Lenna P and based on the Sunshine Coast in Queensland, Australia.
We're quirky, creative and innovative people and would like a business card that keeps you looking for more than just a few seconds.
Design wise we would like a black or charcoal background with a bit of a funkier design than just a boring old rectangle shape. Perhaps curved on an edge.
Ideally we would like to be able to make a collage of all of our best photos on the reverse side of the card with the company name or logo and "catch you round the bend..." (possibly in italics) underneath it.
On the front of the business card we would like our company name -
"Brightwell Studios", our motto- "Bringing Ideas To Life..." (possibly in italics) and our contact information. The background should be a darker colour like black or charcoal.
We like the look of having contact company details and contact info to one side (right) and a black and white photo of Robby K and Lenna P to the other side (left).
Thank you and Good Luck!
Industry/Entity Type
Business
Contact Information for Business Card
Business Name - Brightwell Studios
Slogan - Bring Ideas To life
Name - Robby K | Lenna P
Description - Photography | Videography
Phone - 0438 526 017 | 0412 873 205
Email - brightwellstudios@mailbox.com.au
Website - www.brightwellstudios.com.au
Logo styles of interest
Pictorial/Combination Logo
Look and feel

```html
<!DOCTYPE html>
<html lang="en">
<head>
<meta charset="utf-8">
<title>Brightwell Studios – Business Card</title>
<link href="https://fonts.googleapis.com/css2?family=Didact+Gothic&display=swap" rel="stylesheet">
<style>
  :root {
    --page-bg: #e6e3df;
    --card-dark: #161616;
    --card-mid: #2a2a2a;
    --ink-white: #f4f4f4;
    --ink-grey: #8a8a8a;
    --accent-blue: #21a7dc;
    --photo-light: #b9b5ae;
    --photo-dark: #3a3835;
  }
  * { box-sizing: border-box; margin: 0; padding: 0; }
  html, body { width: 1200px; height: 1000px; overflow: hidden; }
  body {
    background: var(--page-bg);
    font-family: "Didact Gothic", "Century Gothic", sans-serif;
    position: relative;
  }
  .card {
    position: absolute;
    top: 230px;
    width: 540px;
    height: 540px;
    border-radius: 32px;
    background: radial-gradient(circle at 50% 35%, var(--card-mid), var(--card-dark) 75%);
    box-shadow: 0 8px 24px rgba(0,0,0,.25);
    color: var(--ink-white);
    overflow: hidden;
  }
  .card--front { left: 40px; }
  .card--back { left: 620px; }

  /* front */
  .front__title {
    position: absolute; top: 34px; left: 40px; right: 30px;
    font-size: 50px; line-height: 1; letter-spacing: .5px;
  }
  .front__motto {
    position: absolute; top: 92px; left: 92px;
    font-size: 22px; color: var(--ink-white);
  }
  .front__photo {
    position: absolute; top: 132px; left: 40px;
    width: 190px; height: 260px;
    background: linear-gradient(160deg, var(--photo-light), var(--photo-dark));
  }
  .front__names {
    position: absolute; top: 200px; left: 250px;
    font-size: 34px; color: var(--accent-blue); white-space: nowrap;
  }
  .front__roles {
    position: absolute; top: 246px; left: 250px;
    font-size: 20px; color: var(--ink-grey); white-space: nowrap;
  }
  .contact-list {
    position: absolute; right: 34px; bottom: 40px;
    list-style: none; text-align: right;
    font-size: 19px; line-height: 1.75;
  }
  .contact-list li { display: flex; justify-content: flex-end; align-items: center; gap: 10px; }
  .contact-icon { width: 18px; height: 18px; flex: none; }
  .contact-icon * { fill: none; stroke: var(--accent-blue); stroke-width: 2; stroke-linecap: round; stroke-linejoin: round; }
  .contact-icon .solid { fill: var(--accent-blue); stroke: none; }

  /* back */
  .brand-mark {
    position: absolute; top: 200px; left: 0; right: 0;
    display: flex; justify-content: center; align-items: center; gap: 16px;
  }
  .brand-mark__dot {
    width: 34px; height: 34px; border-radius: 50%;
    background: var(--ink-white);
  }
  .brand-mark__name { font-size: 46px; color: var(--ink-white); }
  .back__tagline {
    position: absolute; top: 420px; left: 0; right: 0;
    text-align: center; font-size: 32px;
  }
</style>
</head>
<body>
  <section class="card card--front">
    <h1 class="front__title">Brightwell Studios</h1>
    <p class="front__motto">Bringing Ideas To Life...</p>
    <div class="front__photo" role="img" aria-label="Black and white portrait of Robby K and Lenna P"></div>
    <p class="front__names">Robby K | Lenna P</p>
    <p class="front__roles">Photography | Videography</p>
    <ul class="contact-list">
      <li>0438 526 017 | 0412 873 205
        <svg class="contact-icon" viewBox="0 0 20 20"><path d="M4 2l4 1 1 4-2 2a11 11 0 0 0 4 4l2-2 4 1 1 4-2 2C9 18 2 11 2 4z"/></svg></li>
      <li>brightwellstudios@mailbox.com.au
        <svg class="contact-icon" viewBox="0 0 20 20"><rect x="2" y="4" width="16" height="12"/><path d="M2 4l8 7 8-7"/></svg></li>
      <li>www.brightwellstudios.com.au
        <svg class="contact-icon" viewBox="0 0 20 20"><rect x="2" y="8" width="9" height="5" rx="2.5" transform="rotate(-45 6.5 10.5)"/><rect x="9" y="7" width="9" height="5" rx="2.5" transform="rotate(-45 13.5 9.5)"/></svg></li>
      <li>Like us on Snapwall
        <svg class="contact-icon" viewBox="0 0 20 20"><circle class="solid" cx="10" cy="10" r="7"/></svg></li>
    </ul>
  </section>

  <section class="card card--back">
    <div class="brand-mark">
      <span class="brand-mark__dot"></span>
      <span class="brand-mark__name">Brightwell Studios</span>
    </div>
    <p class="back__tagline">catch you round the bend...</p>
  </section>
</body>
</html>
```